Ebook/Booklet Cover: Neue Arbeitswelten
Tolles Miteinander, hat genau gefühlt und erkannt wo ich hin wollte. Und war sehr geduldig, da ich die letzten Informationen zum Buch jetzt erst mit großer Verspätung übermitteln konnte. Gerne jederzeit wieder!
Zielgruppe
Beratung und Training für kleine und mittlere Unternehmen im Bereich Arbeitnehmerschutz (Arbeitssicherheit), Stressprävention und Aufbau von alltagstauglichen Arbeitsabläufen/Strukturen.
In diesem Buchprojekt jetzt trete ich jedoch nicht primär als Unternehmen auf, sondern als Autorin.
Zielgruppe: Bis jetzt Führungskräfte, Geschäftsführer, Personalmanagement in Unternehmen.
Das soll auch so bleiben nur ist mein Plan in Zukunft auch Privatpersonen anzusprechen.
Inhalt des Ebooks:
Ratgeber, Impulsgeber und Informationsvermittler zu den Themen 'Hybrides Arbeiten', 'Arbeiten im Home Office', 'Digitales Arbeiten' .
Einzelne Themen sind jeweils in einem eigenen Ebook.
Titel ist noch in Arbeit. Es sollten jedoch 2 Zeilen sein.
Eines welches das Thema grob beschreibt - zB 'Perspektiven zur Arbeitswelt der Zukunft' (Das bleibt immer gleich) und darunter 'Hybrides Arbeiten' (Das ist bei jedem Thema dann extra)
Es geht inhaltlich darum, welche Folgen haben diese neuen Arbeitssituationen für Körper - Geist und Psyche und wie geht man im Idealfall damit um. Und wie bereiten wir uns für diese enormen Veränderungen in der ZUkunft optimal vor.
Mit dem Ziel, dass sich der Leser Tipps rauspickt die er selbst umsetzen kann zu Hause. Und vielleicht auch eine neue Perspektive in diese neue Arbeitswelt bekommt.
Und auch Unternehmer und Personalverantwortliche haben so einen Leitfaden für die Zukunft.
Man könnte sagen 'Hoch wissenschaftliche Inhalte + gesetzliche Vorgaben (Also teilweise komplizierte + trockene Inhalte) sollen niederschwellig, leicht lesbar und unterhaltsam präsentiert werden.
Aufgabenstellung
Ich mag Klares. Sauberes. Harmonisches. Ein Mix aus 'edel, niveauvoll, professionell' und 'sympathisch, fröhlich, stylisch'
Nichts Überladenes, keine Reizüberflutung.
Und es darf ein klein wenig darf 'Spiritualität' durchkommen - muss aber nicht.
Auf meiner Homepage sieht man eine Kugel zwischen 2 Händen. Diese passt zB sehr gut zu mir: Verbindend, harmonisch, klar, 'rund'.
Ich habe diese Velmora Bildarchiv Datei angefügt - muss aber nicht verwendet werden!
Weiter unten, wo der Regler zu verschieben ist um Vorstellungen einzugrenzen ist mir aufgefallen, dass dies gar nicht so einfach so beschreiben ist ;-). Wenn eine klare Struktur da ist (zB weißer Hintergrund), Farben harmonisch sind darf ein Teil gerne verspielt und bunt sein als Akzent. Aber eben nicht chaotisch überladen.
Vom Typ her bin ich eher 'HIN ZU statt WEG VON'. Ein Buchcover zum Thema 'Durch Entspannung weniger Stress' würde bei mir zB keinen Kopf zeigen der Blitze und Chaos um sich hat. Sondern ein Kopf der entspannte, bunte, fließende Gedanken hat.
Mei, ich hoffe Ihr Kreativen die das lest habt Eure Kristallkugel zum Gedankenlesen dabei,... ist gar nicht so einfach meine Vorstellung in Worte zu fassen :-).
Zur Preisgestaltung in dem Projekt: Ich bin (Wie viele von uns) finanziell recht gebeutelt durch die aktuelle Situation. Daher geht aktuell nur das Minibudget.
Ich plane hier aber Schritt für Schritt mehr zu machen (Als Autorin) in Zukunft und es ist absolut die Möglichkeit einer weiteren Zusammenarbeit vorhanden.
Liebe Grüße an Euch alle!!
Update:
zu viel schwarze Farbe ist nicht so meines ;-), - ich tendiere zu hellen Designs...

```html
<!DOCTYPE html>
<html lang="de">
<head>
<meta charset="utf-8">
<title>Hybrides Arbeiten – Perspektiven zur Arbeitswelt der Zukunft</title>
<link rel="stylesheet" href="https://fonts.googleapis.com/css2?family=Bebas+Neue&family=Barlow:wght@400;500&display=swap">
<style>
  :root {
    --cream: #f5f1e8;
    --stone: #d8d6cd;
    --plum: #573a3f;
    --rust: #b25a1e;
    --edge: #e58a4a;
    --figure-blue: #8a9fd4;
    --figure-yellow: #dfc05e;
    --figure-orange: #ec7a35;
    --figure-navy: #1c2238;
    --figure-beige: #cbc8b6;
    --ground: #a8a69a;
  }
  html, body {
    margin: 0;
    padding: 0;
    width: 837px;
    height: 1200px;
    overflow: hidden;
    background: var(--cream);
  }
  .cover {
    display: block;
    width: 837px;
    height: 1200px;
  }
  .bg-light { fill: var(--cream); }
  .bg-shade { fill: var(--stone); }
  .edge-line { fill: var(--edge); }
  .title-main {
    font-family: "Bebas Neue", "Oswald", sans-serif;
    fill: var(--plum);
    font-size: 178px;
  }
  .title-sub {
    font-family: "Barlow", "Helvetica Neue", sans-serif;
    font-weight: 500;
    fill: var(--rust);
    font-size: 36px;
  }
  .author {
    font-family: "Barlow", "Helvetica Neue", sans-serif;
    font-weight: 400;
    fill: var(--plum);
    font-size: 28px;
  }
  .tagline {
    font-family: "Barlow", "Helvetica Neue", sans-serif;
    font-weight: 500;
    fill: var(--plum);
    font-size: 25px;
  }
  .ground-shadow { fill: var(--ground); opacity: 0.55; }
</style>
</head>
<body>
<svg class="cover" viewBox="0 0 837 1200" xmlns="http://www.w3.org/2000/svg">
  <defs>
    <linearGradient id="officeTones" x1="0" y1="0" x2="0" y2="1">
      <stop offset="0" stop-color="var(--figure-blue)" stop-opacity="0.45"/>
      <stop offset="0.35" stop-color="var(--figure-yellow)" stop-opacity="0.35"/>
      <stop offset="0.7" stop-color="var(--figure-navy)" stop-opacity="0.22"/>
      <stop offset="1" stop-color="var(--figure-beige)" stop-opacity="0.4"/>
    </linearGradient>
    <linearGradient id="homeTones" x1="0" y1="0" x2="0" y2="1">
      <stop offset="0" stop-color="var(--figure-orange)" stop-opacity="0.4"/>
      <stop offset="0.35" stop-color="var(--figure-blue)" stop-opacity="0.4"/>
      <stop offset="0.75" stop-color="var(--figure-navy)" stop-opacity="0.2"/>
      <stop offset="1" stop-color="#ffffff" stop-opacity="0.35"/>
    </linearGradient>
  </defs>

  <rect class="bg-light" x="0" y="0" width="837" height="1200"/>
  <polygon class="bg-shade" points="700,0 837,0 837,1200 277,1200"/>
  <rect class="edge-line" x="0" y="0" width="2" height="1200"/>

  <g class="title">
    <text class="title-main" x="172" y="187" textLength="488" lengthAdjust="spacingAndGlyphs">HYBRIDES</text>
    <text class="title-sub" x="656" y="225" text-anchor="end">Perspektiven</text>
    <text class="title-main" x="176" y="385" textLength="481" lengthAdjust="spacingAndGlyphs">ARBEITEN</text>
    <text class="title-sub" x="656" y="424" text-anchor="end" textLength="439" lengthAdjust="spacingAndGlyphs">zur Arbeitswelt der Zukunft</text>
  </g>

  <text class="author" x="661" y="470" text-anchor="end">Marlene Winter</text>

  <g class="illustration">
    <ellipse class="ground-shadow" cx="220" cy="978" rx="102" ry="12"/>
    <rect class="figure-office" x="150" y="492" width="160" height="486" rx="70"
          fill="url(#officeTones)" role="img"
          aria-label="Illustration: Frau halb in Bürokleidung, halb in Hauskleidung, mit Aktentasche und Laptop"/>
    <ellipse class="ground-shadow" cx="560" cy="1055" rx="132" ry="13"/>
    <rect class="figure-home" x="435" y="580" width="230" height="475" rx="80"
          fill="url(#homeTones)" role="img"
          aria-label="Illustration: Mann halb in Hauskleidung, halb im Hemd, mit Laptop und Aktentasche, neben ihm eine Katze"/>
  </g>

  <g class="tagline-block">
    <text class="tagline" x="64" y="1132" textLength="699" lengthAdjust="spacingAndGlyphs">Ein Ratgeber, Impulsgeber und Informationsvermittler für</text>
    <text class="tagline" x="64" y="1162" textLength="699" lengthAdjust="spacingAndGlyphs">Führungskräfte, Geschäftsführer und Personalmanagement</text>
  </g>
</svg>
</body>
</html>
```